Certificates with Watermark Images

We are looking for a design of One page Certificates with Watermark (background) images where text will be printed over it .
Graphics design is required to reflect the flowing categories:
IPTV (Internet Protocol TV)
VoD (Video on Demand)
Satellite Receiver
Graphics design images for all three categories must be provided to maintain the same them .
Thank you and good luck.
Internet
- Graphics design images for all three categories must be provided to maintain the same them

```html
<!DOCTYPE html>
<html lang="en">
<head>
<meta charset="utf-8">
<title>Certificate of Attendance</title>
<link rel="stylesheet" href="https://fonts.googleapis.com/css2?family=PT+Sans:ital,wght@0,400;1,400;1,700&family=Playball&display=swap">
<style>
  :root {
    --paper: #ffffff;
    --frame: #d6d6d6;
    --frame-line: #bdbdbd;
    --lime: #a9c41d;
    --lime-pale: #eef4cf;
    --lime-soft: #e3ecb0;
    --ink: #111111;
    --ink-grey: #5f5f5f;
    --rule: #8a8a8a;
  }
  html, body {
    margin: 0;
    padding: 0;
    overflow: hidden;
    background: var(--paper);
  }
  .certificate {
    position: relative;
    width: 878px;
    height: 1200px;
    background: var(--paper);
    overflow: hidden;
    font-family: "PT Sans", "Myriad Pro", sans-serif;
  }
  .certificate__art {
    position: absolute;
    inset: 0;
  }
  .certificate__text {
    position: absolute;
    margin: 0;
    line-height: 1;
    white-space: nowrap;
  }
  .title {
    left: 128px;
    top: 192px;
    font-size: 72px;
    font-style: italic;
    color: var(--lime);
  }
  .awarded-to {
    left: 136px;
    top: 344px;
    font-size: 40px;
    font-style: italic;
    color: var(--ink-grey);
  }
  .recipient {
    left: 146px;
    top: 404px;
    font-family: "Playball", cursive;
    font-size: 62px;
    color: var(--ink);
    letter-spacing: 1px;
  }
  .name-rule {
    position: absolute;
    left: 115px;
    top: 463px;
    width: 512px;
    border-top: 1.5px dashed var(--rule);
  }
  .reason {
    left: 123px;
    top: 494px;
    font-size: 38px;
    font-style: italic;
    color: var(--ink-grey);
  }
  .detail {
    left: 128px;
    font-size: 32px;
    font-style: italic;
    color: var(--ink-grey);
  }
  .detail--venue { top: 604px; }
  .detail--duration { top: 652px; }
  .detail__value {
    font-family: "Playball", cursive;
    font-style: normal;
    font-size: 30px;
    color: var(--ink);
    margin-left: 8px;
  }
  .signature {
    position: absolute;
    width: 224px;
    text-align: center;
    color: var(--ink-grey);
    font-style: italic;
  }
  .signature--left { left: 107px; top: 954px; }
  .signature--right { left: 570px; top: 952px; }
  .signature__rule {
    border-top: 1.5px dashed var(--rule);
    margin-bottom: 16px;
  }
  .signature__name {
    font-weight: 700;
    font-size: 18px;
    line-height: 1.15;
  }
  .signature__role {
    font-size: 18px;
    line-height: 1.15;
  }
  .date-block {
    position: absolute;
    left: 380px;
    top: 1068px;
    width: 200px;
    text-align: center;
    color: var(--ink-grey);
    font-style: italic;
    font-size: 18px;
    line-height: 1.15;
  }
  .date-block__label { font-weight: 700; }
</style>
</head>
<body>
<main class="certificate">
  <svg class="certificate__art" width="878" height="1200" viewBox="0 0 878 1200" aria-hidden="false">
    <!-- watermark rings -->
    <g class="watermark" fill="none" stroke="var(--lime-pale)" stroke-width="16">
      <circle cx="433" cy="254" r="186"/>
      <circle cx="436" cy="610" r="182"/>
      <circle cx="436" cy="965" r="182"/>
    </g>
    <g class="watermark-icons" fill="var(--lime-pale)">
      <circle cx="433" cy="254" r="120" role="img" aria-label="Faint satellite dish emblem"/>
      <circle cx="436" cy="610" r="116" role="img" aria-label="Faint film strip emblem"/>
      <circle cx="436" cy="965" r="116" role="img" aria-label="Faint television emblem"/>
    </g>

    <!-- frame -->
    <g class="frame" fill="none">
      <rect x="49" y="47" width="780" height="1103" stroke="var(--frame)" stroke-width="9"/>
      <rect x="62" y="60" width="754" height="1077" stroke="var(--frame-line)" stroke-width="2"/>
    </g>

    <!-- category badges -->
    <g class="badges">
      <g class="badge">
        <circle cx="751" cy="152" r="98" fill="var(--paper)" stroke="var(--frame)" stroke-width="9"/>
        <circle cx="751" cy="152" r="86" fill="none" stroke="var(--frame-line)" stroke-width="2"/>
        <circle cx="751" cy="152" r="68" fill="none" stroke="var(--lime-soft)" stroke-width="8"/>
        <circle cx="751" cy="152" r="48" fill="var(--lime-soft)" role="img" aria-label="Video on demand film strip icon"/>
      </g>
      <g class="badge">
        <circle cx="751" cy="363" r="98" fill="var(--paper)" stroke="var(--frame)" stroke-width="9"/>
        <circle cx="751" cy="363" r="86" fill="none" stroke="var(--frame-line)" stroke-width="2"/>
        <circle cx="751" cy="363" r="68" fill="none" stroke="var(--lime-soft)" stroke-width="8"/>
        <circle cx="751" cy="363" r="48" fill="var(--lime-soft)" role="img" aria-label="IPTV television icon"/>
      </g>
      <g class="badge">
        <circle cx="751" cy="571" r="98" fill="var(--paper)" stroke="var(--frame)" stroke-width="9"/>
        <circle cx="751" cy="571" r="86" fill="none" stroke="var(--frame-line)" stroke-width="2"/>
        <circle cx="751" cy="571" r="68" fill="none" stroke="var(--lime-soft)" stroke-width="8"/>
        <circle cx="751" cy="571" r="48" fill="var(--lime-soft)" role="img" aria-label="Satellite receiver dish icon"/>
      </g>
    </g>
  </svg>

  <h1 class="certificate__text title">Certificate</h1>
  <p class="certificate__text awarded-to">awarded to</p>
  <p class="certificate__text recipient">Martin Hale</p>
  <div class="name-rule"></div>
  <p class="certificate__text reason">for attending an Internet Course</p>
  <p class="certificate__text detail detail--venue">Venue<span class="detail__value">Ashford Hall</span></p>
  <p class="certificate__text detail detail--duration">Duration<span class="detail__value">12hours</span></p>

  <div class="signature signature--left">
    <div class="signature__rule"></div>
    <div class="signature__name">Owen Fisk</div>
    <div class="signature__role">Director</div>
  </div>
  <div class="signature signature--right">
    <div class="signature__rule"></div>
    <div class="signature__name">Owen Fisk</div>
    <div class="signature__role">Director</div>
  </div>

  <div class="date-block">
    <div class="date-block__label">Date</div>
    <div class="date-block__value">22 August 2011</div>
  </div>
</main>
</body>
</html>
```